Torvel, Inc. new buisness cards - brand guide included

We need new business cards. SLEAK SIMPLE FINANCE. They must include a place for NAME, TITLE, CELL, OFFICE PHONE, EMAIL. they also must include our services across the bottom. AIR, OCEAN, FTL, LTL, EXPRESS. for reference this will be being handed to some of the most prestigious shipping companies in a america.

Target Market(s)

Finance and corporate

Contact Information for Business Card

We need new business cards. SLEAK SIMPLE FINANCE. They must include a place for NAME, TITLE, CELL, OFFICE PHONE, EMAIL. they also must include our services across the bottom. AIR, OCEAN, FTL, LTL, EXPRESS.

Requirements
Must have
• We need new business cards. SLEAK SIMPLE FINANCE. They must include a place for NAME, TITLE, CELL, OFFICE PHONE, EMAIL. they also must include our services across the bottom. AIR, OCEAN, FTL, LTL, EXPRESS.
Nice to have
• USE THE COLORS AND LOGO IN THE BRAND GUIDE :)

```html
<!DOCTYPE html>
<html lang="en">
<head>
<meta charset="utf-8">
<title>Torvel, Inc. Business Cards</title>
<link href="https://fonts.googleapis.com/css2?family=PT+Serif:wght@400;700&family=Lato:wght@400;700&display=swap" rel="stylesheet">
<style>
  :root {
    --ink: #1e1e1e;
    --tan: #c4b495;
    --backdrop: #3a3a3a;
    --serif: "PT Serif", Georgia, serif;
    --sans: "Lato", Arial, sans-serif;
  }
  * { box-sizing: border-box; margin: 0; padding: 0; }
  html, body { width: 1200px; height: 1151px; overflow: hidden; }
  body { background: var(--backdrop); position: relative; font-family: var(--sans); }

  .card {
    position: absolute;
    left: 160px;
    width: 880px;
    height: 503px;
  }
  .card-front { top: 45px; background: var(--ink); }
  .card-back { top: 596px; background: var(--tan); color: var(--ink); }

  .card-frame {
    position: absolute;
    inset: 36px;
    border: 1.5px solid var(--tan);
  }
  .card-back .card-frame { border-color: var(--ink); }

  .brand-name {
    position: absolute;
    inset: 0;
    display: flex;
    align-items: center;
    justify-content: center;
    font-family: var(--serif);
    font-weight: 400;
    font-size: 64px;
    letter-spacing: 4px;
    color: var(--tan);
  }

  .identity {
    position: absolute;
    right: 500px;
    top: 188px;
    text-align: right;
  }
  .person-name {
    font-family: var(--serif);
    font-weight: 700;
    font-size: 30px;
    letter-spacing: 1px;
    line-height: 1.1;
  }
  .person-title {
    font-size: 18px;
    margin-top: 4px;
    margin-right: 12px;
  }

  .divider {
    position: absolute;
    left: 405px;
    top: 180px;
    width: 1.5px;
    height: 132px;
    background: var(--ink);
  }

  .contact-list {
    position: absolute;
    left: 440px;
    top: 190px;
    list-style: none;
  }
  .contact-item {
    display: flex;
    align-items: center;
    gap: 14px;
    font-size: 18px;
    line-height: 29px;
  }
  .contact-icon { width: 14px; height: 14px; fill: var(--ink); flex: none; }

  .services {
    position: absolute;
    left: 0;
    right: 0;
    bottom: 25px;
    text-align: center;
  }
  .services-line {
    display: inline-block;
    background: var(--tan);
    padding: 0 10px;
    font-size: 17px;
    font-weight: 700;
    letter-spacing: 5px;
  }
</style>
</head>
<body>
  <section class="card card-front">
    <div class="card-frame"></div>
    <div class="brand-name">Torvel, Inc.</div>
  </section>

  <section class="card card-back">
    <div class="card-frame"></div>

    <div class="identity">
      <p class="person-name">DANIEL HART</p>
      <p class="person-title">Founder &amp; CEO</p>
    </div>

    <div class="divider"></div>

    <ul class="contact-list">
      <li class="contact-item">
        <svg class="contact-icon" viewBox="0 0 24 24"><path d="M6.6 10.8a15.1 15.1 0 0 0 6.6 6.6l2.2-2.2a1 1 0 0 1 1-.25 11.4 11.4 0 0 0 3.6.57 1 1 0 0 1 1 1V20a1 1 0 0 1-1 1A17 17 0 0 1 3 4a1 1 0 0 1 1-1h3.5a1 1 0 0 1 1 1c0 1.25.2 2.45.57 3.57a1 1 0 0 1-.25 1z"/></svg>
        (123) 456-7890
      </li>
      <li class="contact-item">
        <svg class="contact-icon" viewBox="0 0 24 24"><path d="M7 1h10a2 2 0 0 1 2 2v18a2 2 0 0 1-2 2H7a2 2 0 0 1-2-2V3a2 2 0 0 1 2-2zm0 3v14h10V4zm5 15.5a1 1 0 1 0 0 2 1 1 0 0 0 0-2z"/></svg>
        (123) 456-7890
      </li>
      <li class="contact-item">
        <svg class="contact-icon" viewBox="0 0 24 24"><path d="M2 5h20v14H2zm2 2v.5l8 5 8-5V7zm0 2.8V17h16V9.8l-8 5z"/></svg>
        info@yourwebsitehere.com
      </li>
      <li class="contact-item">
        <svg class="contact-icon" viewBox="0 0 24 24"><circle cx="12" cy="12" r="10"/></svg>
        yourwebsitehere.com
      </li>
    </ul>

    <div class="services">
      <span class="services-line">AIR • OCEAN • FTL • LTL • EXPRESS</span>
    </div>
  </section>
</body>
</html>
```